chocolate bar wrapper

Need a design for a new line of chocolate bars being sold at new retail candy store concept called PLINKTREATS. There will be many flavors including Dark Chocolate, Milk Chocolate, Dark Chocolate Espresso, Milk Chocolate Smores, Dark Chocolate Strawberry Champagne, Dark Chocolate Sea Salt, Dark Chocolate Chipotle, etc. Size of bar is 3 inches x 6 5/8 inches.

Please visit PLINKTREATS.EXAMPLE

Industry/Entity Type

Retail

```html
<!DOCTYPE html>
<html lang="en">
<head>
<meta charset="utf-8">
<title>PLINKTREATS Dark Chocolate Wrapper</title>
<link rel="stylesheet" href="https://fonts.googleapis.com/css2?family=Source+Sans+3:wght@400;700;900&display=swap">
<style>
  :root {
    --page: #ffffff;
    --wrapper: #000000;
    --cocoa-band: #3b2414;
    --cocoa-ball: #2a170b;
    --cocoa-ball-light: #5a3620;
    --truffle-dark: #3a2418;
    --truffle-mid: #7a4a33;
    --truffle-light: #a46c50;
    --white: #ffffff;
    --red: #ed1c24;
    --green: #8dc63f;
    --magenta: #ec008c;
    --blue: #27aae1;
    --yellow: #fff200;
    --green-2: #39b54a;
    --brand: #e0218a;
    --ink: #231a14;
  }
  html, body {
    margin: 0;
    padding: 0;
    width: 1091px;
    height: 1200px;
    overflow: hidden;
    background: var(--page);
    font-family: "Source Sans 3", "Myriad Pro", sans-serif;
  }
  .canvas {
    position: relative;
    width: 1091px;
    height: 1200px;
  }
  .wrapper-panel {
    position: absolute;
    left: 242px;
    top: 0;
    width: 546px;
    height: 1200px;
    background: var(--wrapper);
  }
  .flavor-band {
    position: absolute;
    left: 321px;
    top: 319px;
    width: 467px;
    height: 45px;
    background: var(--cocoa-band);
  }
  .cocoa-ball {
    position: absolute;
    left: 297px;
    top: 279px;
    width: 92px;
    height: 92px;
    border-radius: 50%;
    background: radial-gradient(circle at 35% 35%, var(--cocoa-ball-light), var(--cocoa-ball) 70%);
  }
  .flavor-name {
    position: absolute;
    left: 467px;
    top: 325px;
    margin: 0;
    font-size: 28px;
    font-weight: 400;
    line-height: 1.2;
    color: var(--white);
    letter-spacing: 0.2px;
  }
  .flavor-stripes {
    position: absolute;
    left: 695px;
    top: 324px;
    width: 93px;
    height: 40px;
  }
  .truffle-window {
    position: absolute;
    left: 360px;
    top: 376px;
    width: 428px;
    height: 192px;
  }
  .brand-strip {
    position: absolute;
    left: 245px;
    top: 1036px;
    width: 543px;
    height: 49px;
    background: var(--white);
  }
  .brand-name {
    position: absolute;
    left: 515px;
    top: 1012px;
    width: 246px;
    margin: 0;
    text-align: center;
    font-size: 40px;
    font-weight: 900;
    line-height: 1;
    color: var(--brand);
    letter-spacing: 0.5px;
  }
  .brand-tagline {
    position: absolute;
    left: 515px;
    top: 1064px;
    width: 246px;
    margin: 0;
    text-align: center;
    font-size: 13px;
    font-weight: 900;
    color: var(--ink);
    letter-spacing: 0.3px;
  }
  .web-address {
    position: absolute;
    left: 520px;
    top: 1092px;
    width: 240px;
    margin: 0;
    text-align: center;
    font-size: 17px;
    font-weight: 400;
    color: var(--white);
    letter-spacing: 3.5px;
  }
</style>
</head>
<body>
<main class="canvas">
  <section class="wrapper-panel" aria-label="Chocolate bar wrapper front"></section>

  <div class="flavor-band"></div>
  <div class="cocoa-ball" role="img" aria-label="Illustrated chocolate truffle ball"></div>
  <h1 class="flavor-name">Dark Chocolate</h1>

  <svg class="flavor-stripes" viewBox="0 0 93 40" aria-hidden="true">
    <rect x="0" y="0" width="18" height="40" fill="var(--red)"/>
    <rect x="21" y="0" width="12" height="40" fill="var(--green)"/>
    <rect x="37" y="0" width="8" height="40" fill="var(--magenta)"/>
    <rect x="46" y="0" width="11" height="40" fill="var(--blue)"/>
    <rect x="65" y="0" width="11" height="40" fill="var(--yellow)"/>
    <rect x="80" y="0" width="13" height="40" fill="var(--green-2)"/>
  </svg>

  <svg class="truffle-window" viewBox="0 0 428 192" aria-hidden="false">
    <defs>
      <linearGradient id="truffleTones" x1="0" y1="0" x2="1" y2="1">
        <stop offset="0" stop-color="var(--truffle-dark)"/>
        <stop offset="0.5" stop-color="var(--truffle-mid)"/>
        <stop offset="1" stop-color="var(--truffle-light)"/>
      </linearGradient>
    </defs>
    <polygon points="0,0 428,0 428,10 0,10" fill="var(--white)"/>
    <polygon points="4,10 428,10 428,192 61,192" fill="url(#truffleTones)"
             role="img" aria-label="Photo of rows of chocolate truffles in paper cups"/>
  </svg>

  <div class="brand-strip"></div>
  <p class="brand-name">PLINKTREATS</p>
  <p class="brand-tagline">ICE CREAM, CHOCOLATES &amp; CANDY!</p>
  <p class="web-address">plinktreats.example</p>
</main>
</body>
</html>
```